Stationery Design Project for High End Wealth Management Firm

We need a stationery design for our high-end wealth management firm. Our clientele are affluent and our brand is built around providing investment services with world-class service.

The final concepts should provide a business card, letterhead, and envelope.

We like the idea of having text on the front and back and we MUST have black front and back business cards.
For the business card we have the following that needs to be included:
Company Logo & Tagline
Employee Name
Employee title
Employee Email
Website
2 seperate office cities, addresses, and phone numbers
Financial disclosure (small print)

Having black envelopes would be neat, but black is not a must for the envelopes.
Updates

Project Deadline Extended
Reason: To give the concept one more day of revisions.

Project Deadline Extended
Reason: To allow for more concepts and designs.

Target Market(s)

High Net Worth

Industry/Entity Type

Business

Requirements
Must have
• The following disclosure must be on the back of the card in small print:

Investment Advisory Services offered through Harrowgate Asset Partners LLC, a SEC Registered Investment Advisor. Corvane Wealth Management LLC is not affiliated with Harrowgate Asset Partners LLC.

Black business cards are also a must have.

Please utilize each of the 3 components of our logo in the design.

Please use our white background logo elements when designing our letterhead if you need them.
Nice to have
• Please use our company colors when designing. Utilize a combination of the elements of our logo that we have attached.

We are going to be printing our business cards on letterpress.

```html
<!DOCTYPE html>
<html lang="en">
<head>
<meta charset="utf-8">
<title>Corvane Wealth Management – Letterhead</title>
<link rel="stylesheet" href="https://fonts.googleapis.com/css2?family=Open+Sans:wght@400&display=swap">
<style>
  :root {
    --ink: #231f20;
    --gold: #c89458;
    --gold-deep: #b9834a;
    --paper: #fafafa;
    --text: #3a3a3a;
    --signature: #8a4a1c;
    --footer-text: #d9d9d9;
    --mark-faint: #efe7dc;
  }
  * { margin: 0; padding: 0; box-sizing: border-box; }
  html, body { width: 857px; height: 1200px; overflow: hidden; background: var(--paper); }
  body { font-family: "Open Sans", sans-serif; color: var(--text); }
  .letterhead { position: relative; width: 857px; height: 1200px; background: var(--paper); overflow: hidden; }

  .header-wave { position: absolute; top: 0; left: 0; width: 857px; height: 160px; display: block; }
  .brand-name {
    position: absolute; top: 32px; right: 51px;
    font-size: 14px; letter-spacing: 1px; color: var(--gold);
    display: flex; align-items: center; gap: 8px; white-space: nowrap;
  }
  .brand-dot { width: 12px; height: 12px; border-radius: 50%; background: var(--gold); flex: none; }
  .tagline {
    position: absolute; top: 84px; right: 26px;
    font-size: 10.5px; color: #ffffff; white-space: nowrap; letter-spacing: -0.1px;
  }

  .field { position: absolute; font-size: 14.5px; line-height: 1; }
  .blank { display: inline-block; border-bottom: 1px dotted #555; height: 12px; vertical-align: baseline; }
  .date { left: 17px; top: 161px; }
  .date .blank { width: 128px; }
  .date .year { margin-left: 14px; }
  .recipient { left: 17px; width: 217px; }
  .recipient.line-1 { top: 205px; }
  .recipient.line-2 { top: 234px; }
  .recipient.line-3 { top: 262px; }
  .recipient .blank { width: 217px; }
  .subject { left: 21px; top: 302px; }
  .subject .blank { width: 216px; margin-left: 14px; }
  .salutation { left: 21px; top: 328px; }

  .mark-faint {
    position: absolute; left: 388px; top: 530px;
    width: 126px; height: 126px; border-radius: 50%; background: var(--mark-faint);
  }

  .closing { left: 32px; top: 1034px; }
  .signatory { left: 32px; top: 1060px; color: var(--signature); }

  .footer-rule { position: absolute; left: 0; top: 1100px; width: 857px; height: 9px; background: var(--gold-deep); }
  .footer { position: absolute; left: 0; top: 1109px; width: 857px; height: 91px; background: var(--ink); }
  .footer-brand {
    position: absolute; left: 11px; top: 43px;
    font-size: 8px; letter-spacing: 0.3px; color: var(--gold);
    display: flex; align-items: center; gap: 5px; white-space: nowrap;
  }
  .footer-brand .brand-dot { width: 8px; height: 8px; }
  .contact { position: absolute; left: 183px; font-size: 10.5px; color: var(--footer-text); line-height: 1.1; }
  .contact.address { top: 32px; }
  .contact.phone { top: 64px; }
  .contact .label { display: inline-block; width: 42px; }
  .contact .value { display: inline-block; vertical-align: top; }
</style>
</head>
<body>
<main class="letterhead">
  <svg class="header-wave" viewBox="0 0 1000 187" preserveAspectRatio="none" aria-hidden="true">
    <path fill="#231f20" d="M0 0 H1000 V132 C930,160 870,180 820,180 C640,180 380,76 200,78 C100,80 30,118 0,148 Z"/>
    <path fill="#c89458" d="M0 0 H1000 V124 C930,152 870,172 820,172 C640,172 380,66 200,68 C100,70 30,108 0,138 Z"/>
    <path fill="#231f20" d="M0 0 H1000 V114 C930,142 870,162 820,162 C640,162 380,55 200,57 C100,59 30,98 0,128 Z"/>
  </svg>
  <div class="brand-name"><span class="brand-dot"></span>CORVANE WEALTH MANAGEMENT</div>
  <div class="tagline">Preferred Wealth Management for Select Individuals</div>

  <div class="field date"><span class="blank"></span>,<span class="year">2012</span></div>
  <div class="field recipient line-1"><span class="blank"></span></div>
  <div class="field recipient line-2"><span class="blank"></span></div>
  <div class="field recipient line-3"><span class="blank"></span></div>
  <div class="field subject">Re: Follow Up Report For<span class="blank"></span></div>
  <div class="field salutation">Dear Mr. :</div>

  <div class="mark-faint" aria-hidden="true"></div>

  <div class="field closing">Sincerely,</div>
  <div class="field signatory">R. Halden</div>

  <div class="footer-rule"></div>
  <footer class="footer">
    <div class="footer-brand"><span class="brand-dot"></span>CORVANE WEALTH MANAGEMENT</div>
    <div class="contact address"><span class="label">Address</span><span class="value">: Loreum Ipsum Dollar,<br>&nbsp;&nbsp;Loreum Ipsum</span></div>
    <div class="contact phone"><span class="label">Phone</span><span class="value">: +9714 555 0182</span></div>
  </footer>
</main>
</body>
</html>
```